Business Card Design for Retail Product Line

We need a two-sided, full-color business card for a new oral care product line. The feel of the card should invoke emotions of happiness and health. It should be bright, cheerful and modern in appearance. The card should be mostly matte finish, but with elements of spot-gloss and/or raised/embossed features (print, logo, tag lines, etc.).

Target Market(s)

People who are into whole-body health, eat well and understand the importance of nutrition.

Industry/Entity Type

Health And Wellness

Contact Information for Business Card

The logo, color scheme and tag-lines have all been developed and artwork is attached. Card is to be standard-sized and should use a mix of clean, sans-serif fonts; the main font (DIN) is attached as well. The card will be used for 3 individuals and should include placeholders for:
1. Name
2. Title (for example, "CEO")
3. Business address
4. Phone number
5. Website
6. Email address

Font styles to use
Sans Serif
Other font styles liked:
• DIN font

Colors
faa54b
000000
5c5c5c
a2ce44

Requirements
Must have
• 2 sides
• Full color orange on one side
• Image of DNA leaves
• Tag line "Glow from the Root Upward", on single side with orange background
• Company Logo (Plome) on same side as text (name, phone, address, etc.)
• Name, Title, Business Address, Phone Number, Website, Email address
• UPDATE: "Brisk Marrow", not "Brisk M Arrow"
Should not have
• Calligraphy
• Dark colors
• UPDATE!! Do not include "Turmeric infused toothpaste" on the business card
• UPDATE #2!! Do not include "Brisk Marrow" on the business card

```html
<!DOCTYPE html>
<html lang="en">
<head>
<meta charset="utf-8">
<title>Plome Business Card</title>
<link rel="stylesheet" href="https://fonts.googleapis.com/css2?family=Barlow:wght@400;500;600;700;800&display=swap">
<style>
  :root {
    --orange: #faa54b;
    --gold-edge: #e89a32;
    --gold-mid: #f2cc3e;
    --ink: #000000;
    --grey: #5c5c5c;
    --leaf: #a2ce44;
    --leaf-deep: #1f9a3e;
    --helix-grey: #c9c9c9;
    --white: #ffffff;
    --backdrop: #ece9e4;
  }
  * { margin: 0; padding: 0; box-sizing: border-box; }
  html, body {
    width: 1200px;
    height: 1076px;
    overflow: hidden;
    background: var(--backdrop);
    font-family: "Barlow", sans-serif;
  }
  .canvas {
    position: relative;
    width: 1200px;
    height: 1076px;
  }
  .card {
    position: absolute;
    left: 170px;
    width: 860px;
    height: 496px;
    overflow: hidden;
    box-shadow: 0 6px 18px rgba(0, 0, 0, 0.18);
  }

  /* Front side */
  .card--front {
    top: 28px;
    background: linear-gradient(155deg, var(--gold-edge) 0%, var(--gold-mid) 42%, var(--gold-mid) 58%, var(--gold-edge) 100%);
  }
  .brand-name {
    position: absolute;
    left: 0;
    right: 0;
    top: 180px;
    text-align: center;
    font-weight: 700;
    font-size: 132px;
    line-height: 1;
    color: var(--white);
    letter-spacing: -1px;
  }

  /* Back side */
  .card--back {
    top: 552px;
    background: var(--orange);
  }
  .dna-leaves {
    position: absolute;
    left: 0;
    top: 0;
    width: 330px;
    height: 496px;
    background: linear-gradient(180deg, var(--leaf) 0%, var(--leaf-deep) 45%, var(--leaf) 62%, var(--helix-grey) 80%, var(--helix-grey) 100%);
    border-radius: 0 160px 160px 0;
  }
  .back-brand {
    position: absolute;
    left: 410px;
    top: 30px;
    font-weight: 700;
    font-size: 40px;
    line-height: 1.1;
    color: var(--white);
  }
  .contact {
    position: absolute;
    left: 410px;
    top: 112px;
    width: 406px;
    color: var(--ink);
  }
  .contact__name {
    font-weight: 700;
    font-size: 32px;
    line-height: 1.1;
  }
  .contact__title {
    font-weight: 500;
    font-size: 20px;
    line-height: 1.1;
  }
  .contact__rule {
    border: none;
    border-top: 3px dotted var(--ink);
    margin: 16px 0 20px;
  }
  .contact__line {
    font-weight: 500;
    font-size: 21px;
    line-height: 32px;
  }
  .contact__label { font-weight: 700; }
  .contact__address {
    font-weight: 500;
    font-size: 21px;
    line-height: 29px;
  }
  .back-tagline {
    position: absolute;
    left: 410px;
    top: 436px;
    font-weight: 700;
    font-size: 24px;
    line-height: 1.2;
    color: var(--white);
    letter-spacing: 0.3px;
  }
</style>
</head>
<body>
  <main class="canvas">
    <section class="card card--front" aria-label="Card front">
      <div class="brand-name">Plome</div>
    </section>

    <section class="card card--back" aria-label="Card back">
      <div class="dna-leaves" role="img" aria-label="Illustration of a DNA helix growing green leaves"></div>
      <div class="back-brand">Plome</div>
      <div class="contact">
        <h1 class="contact__name">Dana Ellery</h1>
        <p class="contact__title">CEO</p>
        <hr class="contact__rule">
        <p class="contact__line"><span class="contact__label">Phone:</span> (555).555.0142</p>
        <p class="contact__line"><span class="contact__label">Email:</span> hello@plomecare.com</p>
        <p class="contact__line"><span class="contact__label">Web:</span> www.plomecare.com</p>
        <hr class="contact__rule">
        <p class="contact__address">210 Fernhill Road, 2nd Ste<br>Alder Bay, Oregon 5821, USA</p>
      </div>
      <p class="back-tagline">Glow from the Root Upward</p>
    </section>
  </main>
</body>
</html>
```